Thank You For Shopping / Hair Care Tips

I need “Thank You For Shopping”
Post cards made for my hair business !
I added pictures of post cards that I really like . I also added my LuzeKora Wigs logo for you guys to use

I want the backside of the flyer to have hair care tips !
I want people to have full directions on how to care for their wigs

Target Market(s)

Im marking to young woman to older middle aged woman
Ages 23-66 . I want my flyer to look mature And classy

Industry/Entity Type

Hair And Beauty

Font styles to use
Serif
Script

Colors
e34699
e34298
e34398

Requirements
Must have
• The flyer must have the Instagram logo with my Instagram name next to it @luze.kora.wigs__
• Also it must have my “Luze Kora Wigs” logo that I’ve uploaded in the pictures section .
• Flyer had to be two sides . One side “ thank you for shopping “ side two “hair care tips”
• My website must be on the flyer - www.luzekorawigs.example
• The flyer must match the colors of my logo
• All white . With the pink and glitter sliver you see on my logo
Nice to have
• Nice to have a glitter border
Should not have
• The flyer should not have different colors that don’t match my logo
• It shouldn’t be made without having my Instagram or website on the flyer

```html
<!DOCTYPE html>
<html lang="en">
<head>
<meta charset="utf-8">
<title>Luze Kora Wigs – Thank You Postcard</title>
<link rel="stylesheet" href="https://fonts.googleapis.com/css2?family=Lato:wght@400;700&family=Permanent+Marker&family=Kaushan+Script&display=swap">
<style>
  :root {
    --stage: #434243;
    --pink: #e34398;
    --ink: #1a1a1a;
    --white: #ffffff;
    --frame-dark: #6b6b6b;
    --frame-light: #a9a9a9;
    --sparkle: #e6e6e6;
  }
  * { box-sizing: border-box; margin: 0; padding: 0; }
  html, body { width: 1200px; height: 1200px; overflow: hidden; }
  body { background: var(--stage); font-family: "Lato", sans-serif; color: var(--ink); position: relative; }

  .card {
    position: absolute; left: 280px; width: 636px; height: 494px;
    box-shadow: 0 10px 26px rgba(0,0,0,.45);
  }
  .card--front { top: 82px; }
  .card--back { top: 621px; height: 491px; }

  .glitter-frame {
    position: absolute; inset: 0;
    background: linear-gradient(135deg, var(--frame-dark), var(--frame-light) 30%, var(--frame-dark) 55%, var(--frame-light) 80%, var(--frame-dark));
  }
  .card-face {
    position: absolute; inset: 16px; overflow: hidden;
    background: linear-gradient(180deg, var(--sparkle) 0%, var(--white) 22%, var(--white) 65%, var(--sparkle) 100%);
  }
  .card--back .card-face {
    background: linear-gradient(180deg, var(--sparkle) 0%, var(--white) 30%, var(--white) 75%, var(--sparkle) 100%);
  }

  .abs { position: absolute; }

  .brand-name {
    left: 0; right: 0; top: 86px; text-align: center;
    font-family: "Lato", sans-serif; font-weight: 700; font-size: 40px; line-height: 1;
    color: var(--pink); letter-spacing: 1px; white-space: nowrap;
  }
  .thank-you {
    left: 0; right: 0; top: 180px; height: 108px; text-align: center;
    font-family: "Permanent Marker", cursive; font-size: 96px; line-height: 108px;
    color: var(--pink); letter-spacing: -1px; white-space: nowrap; padding-left: 20px;
    font-weight: 400;
  }
  .thanks-rule { left: 64px; top: 320px; width: 206px; height: 3px; background: var(--pink); }
  .thanks-sub {
    left: 282px; top: 296px; line-height: 46px;
    font-family: "Kaushan Script", cursive; font-size: 38px; color: var(--ink); white-space: nowrap;
  }

  .contact { display: flex; align-items: center; gap: 7px; font-weight: 700; font-size: 19px; line-height: 24px; color: var(--ink); white-space: nowrap; }
  .contact svg { flex: none; }
  .front-web { left: 0; right: 0; top: 374px; justify-content: center; }
  .front-social { left: 0; right: 0; top: 402px; justify-content: center; padding-left: 30px; }

  .tips-band {
    left: 0; right: 0; top: 49px; height: 60px; background: var(--pink);
    display: flex; align-items: center; justify-content: center;
  }
  .tips-title {
    font-family: "Permanent Marker", cursive; font-size: 44px; line-height: 1; color: var(--white);
    font-weight: 400; transform: skewX(-8deg); letter-spacing: 1px; padding-right: 20px; white-space: nowrap;
  }
  .tips-divider { left: 297px; top: 155px; width: 2px; height: 192px; background: var(--pink); }

  .tip { display: flex; gap: 4px; width: 258px; font-size: 13.5px; line-height: 17px; }
  .tip svg { flex: none; margin-top: 0; }
  .tip--l1 { left: 16px; top: 122px; }
  .tip--l2 { left: 16px; top: 222px; }
  .tip--l3 { left: 16px; top: 318px; }
  .tip--r1 { left: 342px; top: 124px; width: 248px; }
  .tip--r2 { left: 342px; top: 226px; width: 248px; }
  .tip--r3 { left: 342px; top: 312px; width: 248px; }

  .back-web { left: 62px; top: 420px; }
  .back-social { left: 334px; top: 420px; }
</style>
</head>
<body>

<svg width="0" height="0" style="position:absolute">
  <defs>
    <symbol id="icon-globe" viewBox="0 0 20 20">
      <g fill="none" stroke="#e34398" stroke-width="1.4">
        <circle cx="10" cy="10" r="8"/>
        <ellipse cx="10" cy="10" rx="3.6" ry="8"/>
        <path d="M2 10h16M3.5 6h13M3.5 14h13"/>
      </g>
    </symbol>
    <symbol id="icon-dot" viewBox="0 0 20 20">
      <circle cx="10" cy="10" r="7.5" fill="#e34398"/>
    </symbol>
    <symbol id="icon-tick" viewBox="0 0 26 22">
      <g fill="none" stroke="#e34398" stroke-width="2">
        <rect x="1.5" y="5" width="15" height="15"/>
        <path d="M5 11l4.5 5L24 2"/>
      </g>
    </symbol>
  </defs>
</svg>

<section class="card card--front">
  <div class="glitter-frame" role="img" aria-label="Silver glitter border"></div>
  <div class="card-face" role="img" aria-label="White background with soft silver glitter">
    <div class="abs brand-name">Luze Kora Wigs</div>
    <h1 class="abs thank-you">THANK YOU</h1>
    <div class="abs thanks-rule"></div>
    <p class="abs thanks-sub">For Shopping</p>
    <p class="abs contact front-web"><svg width="18" height="18"><use href="#icon-globe"/></svg>www.luzekorawigs.example</p>
    <p class="abs contact front-social"><svg width="16" height="16"><use href="#icon-dot"/></svg>@luze.kora.wigs</p>
  </div>
</section>

<section class="card card--back">
  <div class="glitter-frame" role="img" aria-label="Silver glitter border"></div>
  <div class="card-face" role="img" aria-label="White background with soft silver glitter">
    <div class="abs tips-band"><h2 class="tips-title">HAIR CARE TIPS</h2></div>

    <p class="abs tip tip--l1"><svg width="26" height="22"><use href="#icon-tick"/></svg><span>Lorem ipsum is placeholder text commonly used in the graphic, print, and publishing industries for previewing layouts and visual mockups.</span></p>
    <p class="abs tip tip--l2"><svg width="26" height="22"><use href="#icon-tick"/></svg><span>Lorem ipsum is placeholder text commonly used in the graphic, print, and publishing industries for previewing layouts and visual mockups.</span></p>
    <p class="abs tip tip--l3"><svg width="26" height="22"><use href="#icon-tick"/></svg><span>Lorem ipsum is placeholder text commonly used in the graphic, print, and publishing industries for</span></p>

    <div class="abs tips-divider"></div>

    <p class="abs tip tip--r1"><svg width="26" height="22"><use href="#icon-tick"/></svg><span>Lorem ipsum is placeholder text commonly used in the graphic, print, and publishing industries for previewing layouts and visual mockups.</span></p>
    <p class="abs tip tip--r2"><svg width="26" height="22"><use href="#icon-tick"/></svg><span>Lorem ipsum is placeholder text commonly used in the graphic, print, and publishing industries for previewing layouts and visual</span></p>
    <p class="abs tip tip--r3"><svg width="26" height="22"><use href="#icon-tick"/></svg><span>Lorem ipsum is placeholder text commonly used in the graphic, print, and publishing industries for</span></p>

    <p class="abs contact back-web"><svg width="16" height="16"><use href="#icon-globe"/></svg>www.luzekorawigs.example</p>
    <p class="abs contact back-social"><svg width="16" height="16"><use href="#icon-dot"/></svg>@luze.kora.wigs</p>
  </div>
</section>

</body>
</html>
```